Webdesign für Freelancer Web/App (OnePager)
Zielgruppe
Ich bin ein Freelancer im Bereich Web- und App-Entwicklung. Über eine professionelle Webseite möchte ich neue Kunden gewinnen. Dazu möchte ich mich und meine Leistungen vorstellen und dem Benutzer die Möglichkeit bieten meine Arbeiten anzuschauen und mich zu kontaktieren.
Aufgabenstellung
Optisch gefallen mir Onepager sehr gut (z.B. http://muster.veltora.com/). Ich möchte mir aber offen halten, auch mehrere Unterseiten zu erstellen. Inhaltlich kann man sich bspw. an https://www.quintelor.ch/ orientieren.
Es geht ausschliesslich um die Umsetzung des Webdesigns.
Es sind bereits ein Logo, eine Schrift und 2 Farben definiert. Nur das Blau muss verwendet werden, das grün ist optional. Weitere Farben und 1 weitere Schrift dürfen verwendet werden. Das Logo darf mit oder ohne Schriftzug verwendet werden. Freie Stock-Fotos dürfen verwendet werden. Das Design muss auf Desktop (optimiert auf ca. 1400px) und Mobile funktionieren (Responsive). Nice to have wären optimierte App- und Favicons die auch vom Logo abweichen dürfen. Nice to have wäre ein Fendora Map Pin.

```html
<!DOCTYPE html>
<html lang="de">
<head>
<meta charset="utf-8">
<title>Timo Raske – Web &amp; App Entwickler</title>
<link href="https://fonts.googleapis.com/css2?family=Open+Sans:ital,wght@0,400;0,600;0,700;1,400;1,600&family=Raleway:wght@300;400;700&display=swap" rel="stylesheet">
<style>
:root{
  --blue:#2a68a8;
  --navy:#173a63;
  --ink:#1b3a60;
  --text:#3a4656;
  --muted:#6b7686;
  --orange:#f06a32;
  --mist:#e4e7ee;
  --hero:#e2e5eb;
  --white:#fff;
}
*{box-sizing:border-box;margin:0;padding:0}
html,body{width:1200px;height:3309px;overflow:hidden}
body{position:relative;background:var(--white);font-family:"Open Sans",sans-serif;color:var(--text)}
.abs{position:absolute}
.center{left:0;width:1200px;text-align:center}
.logo{font-family:"Open Sans",sans-serif;font-weight:700;color:var(--navy);font-size:24px;letter-spacing:1px;display:flex;align-items:center;gap:6px}
.logo i{display:inline-block;width:10px;height:10px;background:var(--navy)}
.nav{top:28px;right:133px;display:flex;gap:13px;font-size:13px;letter-spacing:1px;color:var(--ink)}
.nav b{font-weight:700;margin-right:10px}
.hero{top:0;left:0;width:1200px;height:593px;background:var(--hero)}
.hero-photo{top:60px;left:560px;width:530px;height:533px;background:radial-gradient(ellipse at 55% 45%,#f3f4f6 0%,#d8dce3 55%,#e2e5eb 100%)}
.headline{top:200px;left:132px;font-family:"Raleway",sans-serif;font-weight:300;font-size:42px;line-height:51px;color:#111}
.headline b{font-weight:700}
.lead{top:409px;left:132px;font-size:12.5px;line-height:20px;color:#222}
.btn{display:flex;align-items:center;justify-content:center;font-size:12.5px}
.btn-blue{background:var(--blue);color:var(--white)}
.btn-line{border:1.5px solid #555;color:#333}
.h2{font-weight:700;font-size:20px;color:var(--ink);letter-spacing:.5px}
.sub{font-size:10px;line-height:16px;color:var(--text)}
.svc{width:310px;text-align:center}
.svc svg{display:block;margin:0 auto}
.svc h3{font-size:11.5px;font-weight:700;color:var(--ink);margin-top:14px;letter-spacing:.3px}
.svc p{font-size:9.5px;line-height:16px;color:var(--muted);margin-top:14px}
.ref{width:224px}
.ref .img{height:223px}
.ref h4{font-size:12px;font-weight:700;color:#222;margin-top:13px}
.ref h4 span{font-weight:400;font-size:9.5px;color:var(--blue);margin-left:6px}
.ref .client{font-size:9px;color:#333;margin-top:5px;padding-bottom:9px;border-bottom:1px solid #dde0e5}
.ref .client b{font-weight:700}
.ref .tags{font-size:12px;color:var(--orange);margin-top:9px;word-spacing:3px}
.band{left:0;width:1200px;background:var(--mist)}
.quote{font-style:italic;font-size:16.5px;line-height:24px;color:var(--ink)}
.skill{width:289px}
.skill span{font-style:italic;font-size:9px;color:var(--ink)}
.skill .bar{height:3px;background:var(--white);margin-top:6px}
.skill .bar i{display:block;height:3px;background:var(--orange)}
.contact{top:2678px;left:0;width:1200px;height:567px;background:var(--navy);color:#c9d3e0}
.contact .h2{color:var(--white)}
.field{border-bottom:1px solid #5c7597;font-style:italic;font-weight:600;font-size:9.5px;color:var(--white)}
.footer{top:3245px;left:0;width:1200px;height:64px;background:var(--white)}
</style>
</head>
<body>

<header class="hero abs">
  <div class="hero-photo abs" role="img" aria-label="Porträtfoto eines Entwicklers im weissen Hemd mit Krawatte"></div>
  <div class="logo abs" style="top:24px;left:133px"><i></i>TIRA</div>
  <nav class="nav abs"><b>HOME</b><span>LEISTUNGEN</span><span>REFERENZEN</span><span>ÜBER MICH</span><span>KONTAKT</span></nav>
  <h1 class="headline abs">Ich bin Timo Raske,<br>ein <b>Entwickler</b><br>aus St.Gallen,<br>Schweiz</h1>
  <p class="lead abs">Entwicklung in den Bereichen <b>Web</b> und <b>Apps</b> sind meine Schwerpunkte.<br>Lorem ipsum dolor sit amet, consetetur sadipscing elitr.</p>
  <a class="btn btn-blue abs" style="top:463px;left:133px;width:133px;height:35px">Meine Referenzen</a>
  <a class="btn btn-line abs" style="top:463px;left:279px;width:133px;height:35px">Meine Leistungen</a>
</header>

<section>
  <h2 class="h2 abs center" style="top:615px">LEISTUNGEN</h2>
  <p class="sub abs center" style="top:649px">At vero eos et accusam et justo duo dolores et ea rebum. Stet clita kasd gubergren,<br>no sea takimata sanctus est Lorem ipsum dolor sit amet.</p>

  <div class="svc abs" style="top:698px;left:134px">
    <svg width="56" height="34" viewBox="0 0 56 34"><circle cx="28" cy="12" r="7" fill="none" stroke="var(--blue)" stroke-width="1.4"/><path d="M25 19v5h6v-5" fill="none" stroke="var(--blue)" stroke-width="1.4"/><line x1="0" y1="32" x2="56" y2="32" stroke="var(--orange)" stroke-width="1.5"/></svg>
    <h3>BERATUNG &amp; KONZEPT</h3>
    <p>Lorem ipsum dolor sit amet, consetetur sadipscing<br>elitr, sed diam nonumy eirmod tempor invidunt ut<br>labore et dolore magna aliquyam erat.</p>
  </div>
  <div class="svc abs" style="top:698px;left:440px">
    <svg width="56" height="34" viewBox="0 0 56 34"><path d="M20 24l4-8 10-10 2 2-10 10z" fill="none" stroke="var(--blue)" stroke-width="1.4"/><circle cx="31" cy="12" r="2" fill="var(--blue)"/><line x1="0" y1="32" x2="56" y2="32" stroke="var(--orange)" stroke-width="1.5"/></svg>
    <h3>WEBDESIGN &amp; ENTWICKLUNG</h3>
    <p>Lorem ipsum dolor sit amet, consetetur sadipscing<br>elitr, sed diam nonumy eirmod tempor invidunt ut<br>labore et dolore magna aliquyam erat.</p>
  </div>
  <div class="svc abs" style="top:698px;left:754px">
    <svg width="56" height="34" viewBox="0 0 56 34"><path d="M20 10h6v-4h6v4h4v6h-4v6h-6v-4h-6z" fill="none" stroke="var(--blue)" stroke-width="1.4"/><line x1="0" y1="32" x2="56" y2="32" stroke="var(--orange)" stroke-width="1.5"/></svg>
    <h3>CONTENT MANAGEMENT SYSTEME (CMS)</h3>
    <p>Lorem ipsum dolor sit amet, consetetur sadipscing<br>elitr, sed diam nonumy eirmod tempor invidunt ut<br>labore et dolore magna aliquyam erat.</p>
  </div>

  <div class="svc abs" style="top:865px;left:134px">
    <svg width="56" height="34" viewBox="0 0 56 34"><path d="M20 26l2-6 12-12 4 4-12 12z" fill="none" stroke="var(--blue)" stroke-width="1.4"/><line x1="0" y1="32" x2="56" y2="32" stroke="var(--orange)" stroke-width="1.5"/></svg>
    <h3>FRAMEWORK-ENTWICKLUNG</h3>
    <p>Lorem ipsum dolor sit amet, consetetur sadipscing<br>elitr, sed diam nonumy eirmod tempor invidunt ut<br>labore et dolore magna aliquyam erat.</p>
  </div>
  <div class="svc abs" style="top:865px;left:440px">
    <svg width="56" height="34" viewBox="0 0 56 34"><rect x="20" y="14" width="10" height="6" rx="3" transform="rotate(-45 25 17)" fill="none" stroke="var(--blue)" stroke-width="1.4"/><rect x="26" y="8" width="10" height="6" rx="3" transform="rotate(-45 31 11)" fill="none" stroke="var(--blue)" stroke-width="1.4"/><line x1="0" y1="32" x2="56" y2="32" stroke="var(--orange)" stroke-width="1.5"/></svg>
    <h3>HYBIRD-APPS MIT CORVANA UND IONARA</h3>
    <p>Lorem ipsum dolor sit amet, consetetur sadipscing<br>elitr, sed diam nonumy eirmod tempor invidunt ut<br>labore et dolore magna aliquyam erat.</p>
  </div>
  <div class="svc abs" style="top:865px;left:754px">
    <svg width="56" height="34" viewBox="0 0 56 34"><rect x="22" y="7" width="11" height="18" rx="1.5" fill="none" stroke="var(--blue)" stroke-width="1.4"/><rect x="29" y="3" width="8" height="8" fill="var(--orange)"/><line x1="0" y1="32" x2="56" y2="32" stroke="var(--orange)" stroke-width="1.5"/></svg>
    <h3>APPS MIT NATIVEKIT</h3>
    <p>Lorem ipsum dolor sit amet, consetetur sadipscing<br>elitr, sed diam nonumy eirmod tempor invidunt ut<br>labore et dolore magna aliquyam erat.</p>
  </div>
</section>

<section>
  <h2 class="h2 abs center" style="top:1043px">REFERENZEN</h2>
  <p class="sub abs center" style="top:1079px">At vero eos et accusam et justo duo dolores et ea rebum. Stet clita kasd gubergren,<br>no sea takimata sanctus est Lorem ipsum dolor sit amet.</p>

  <article class="ref abs" style="top:1132px;left:133px"><div class="img" role="img" aria-label="Fitness-App auf einem Smartphone" style="background:linear-gradient(150deg,#5f6670,#2b3038)"></div><h4>Lorem Ipsum Projekt<span>• Sep 2016</span></h4><p class="client"><b>Kunde:</b> Dolor Set Amet GmbH &amp; Co KG</p><p class="tags">HTML5 CSS3 JS Qlib</p></article>
  <article class="ref abs" style="top:1132px;left:369px"><div class="img" role="img" aria-label="Tablet mit schwebenden App-Symbolen" style="background:linear-gradient(150deg,#f4f4f4,#d9dadc)"></div><h4>Lorem Ipsum Projekt<span>• Sep 2016</span></h4><p class="client"><b>Kunde:</b> Dolor Set Amet GmbH &amp; Co KG</p><p class="tags">HTML5 CSS3 JS Qlib</p></article>
  <article class="ref abs" style="top:1132px;left:606px"><div class="img" role="img" aria-label="Wetter-App Oberfläche in Türkis" style="background:linear-gradient(160deg,#4fcfcf,#1aa3a8)"></div><h4>Lorem Ipsum Projekt<span>• Sep 2016</span></h4><p class="client"><b>Kunde:</b> Dolor Set Amet GmbH &amp; Co KG</p><p class="tags">HTML5 CSS3 JS Qlib</p></article>
  <article class="ref abs" style="top:1132px;left:843px"><div class="img" role="img" aria-label="Mobile App Screens in Petrol" style="background:linear-gradient(150deg,#e9ecee,#9fb7ba)"></div><h4>Lorem Ipsum Projekt<span>• Sep 2016</span></h4><p class="client"><b>Kunde:</b> Dolor Set Amet GmbH &amp; Co KG</p><p class="tags">HTML5 CSS3 JS Qlib</p></article>

  <article class="ref abs" style="top:1474px;left:133px"><div class="img" role="img" aria-label="Tablet mit Flug-App in der Hand" style="background:linear-gradient(150deg,#4a4c52,#1e2329)"></div><h4>Lorem Ipsum Projekt<span>• Sep 2016</span></h4><p class="client"><b>Kunde:</b> Dolor Set Amet GmbH &amp; Co KG</p><p class="tags">HTML5 CSS3 JS Qlib</p></article>
  <article class="ref abs" style="top:1474px;left:369px"><div class="img" role="img" aria-label="Smartphone mit Login-App in der Hand" style="background:linear-gradient(150deg,#e8ecc4,#8eaa86)"></div><h4>Lorem Ipsum Projekt<span>• Sep 2016</span></h4><p class="client"><b>Kunde:</b> Dolor Set Amet GmbH &amp; Co KG</p><p class="tags">HTML5 CSS3 JS Qlib</p></article>
  <article class="ref abs" style="top:1474px;left:606px"><div class="img" role="img" aria-label="Dunkelblaue App-Oberflächen" style="background:linear-gradient(150deg,#2c3b6e,#17567f)"></div><h4>Lorem Ipsum Projekt<span>• Sep 2016</span></h4><p class="client"><b>Kunde:</b> Dolor Set Amet GmbH &amp; Co KG</p><p class="tags">HTML5 CSS3 JS Qlib</p></article>
  <article class="ref abs" style="top:1474px;left:843px"><div class="img" role="img" aria-label="Hand skizziert Wireframes mit Stift" style="background:linear-gradient(150deg,#e6d6c8,#f2f3f5)"></div><h4>Lorem Ipsum Projekt<span>• Sep 2016</span></h4><p class="client"><b>Kunde:</b> Dolor Set Amet GmbH &amp; Co KG</p><p class="tags">HTML5 CSS3 JS Qlib</p></article>
</section>

<section class="band abs" style="top:1800px;height:308px" role="img" aria-label="Heller Schreibtisch mit Notizbuch und Tastatur als Hintergrund">
  <p class="abs center" style="top:24px;font-size:11.5px;font-weight:700;color:var(--ink)">WAS MEINE KUNDEN SAGEN</p>
  <p class="abs center" style="top:51px;font-size:9.5px;color:var(--muted)">Lorem ipsum dolor sit amet, consetetur sadipscing elitr, sed diam nonumy eirmod tempor invidunt.</p>
  <p class="quote abs center" style="top:91px">„Lorem ipsum dolor sit amet, consetetur sadipscing elitr, sed<br>diam nonumy eirmod tempor invidunt ut labore et dolore<br>magna aliquyam erat, sed diam voluptua. At vero eos et ac-<br>cusam.. “</p>
  <svg class="abs" style="top:204px;left:573px" width="54" height="2"><rect width="27" height="2" fill="var(--blue)"/><rect x="27" width="27" height="2" fill="var(--orange)"/></svg>
  <p class="abs center" style="top:233px;font-size:10.5px;font-weight:700;color:var(--orange)">MAX MUSTERMANN</p>
  <p class="abs center" style="top:249px;font-size:11px;color:var(--text)">Lorem Ipsum</p>
  <svg class="abs" style="top:273px;left:580px" width="40" height="10"><circle cx="5" cy="5" r="4" fill="#fff"/><circle cx="20" cy="5" r="3.5" fill="none" stroke="#fff"/><circle cx="35" cy="5" r="3.5" fill="none" stroke="#fff"/></svg>
  <svg class="abs" style="top:142px;left:132px" width="16" height="26"><path d="M14 1L2 13l12 12" fill="none" stroke="#fff" stroke-width="2"/></svg>
  <svg class="abs" style="top:142px;left:1052px" width="16" height="26"><path d="M2 1l12 12L2 25" fill="none" stroke="#fff" stroke-width="2"/></svg>
</section>

<section>
  <div class="abs" role="img" aria-label="Porträtfoto des Entwicklers" style="top:2129px;left:539px;width:122px;height:122px;border-radius:50%;background:radial-gradient(circle at 50% 40%,#e8d3c3,#8a7060)"></div>
  <h2 class="h2 abs center" style="top:2256px">ÜBER MICH</h2>
  <p class="sub abs center" style="top:2294px">At vero eos et accusam et justo duo dolores et ea rebum. Stet clita kasd gubergren,<br>no sea takimata sanctus est Lorem ipsum dolor sit amet.</p>
  <a class="btn btn-blue abs" style="top:2347px;left:533px;width:133px;height:35px">Mehr über mich</a>
</section>

<section class="band abs" style="top:2412px;height:266px">
  <h2 class="h2 abs center" style="top:27px">MEINE SKILLS</h2>
  <p class="sub abs center" style="top:64px">At vero eos et accusam et justo duo dolores et ea rebum. Stet clita kasd gubergren,<br>no sea takimata sanctus est Lorem ipsum dolor sit amet.</p>
  <div class="skill abs" style="top:130px;left:133px"><span>HTML 5</span><div class="bar"><i style="width:94%"></i></div></div>
  <div class="skill abs" style="top:130px;left:455px"><span>JavaScript</span><div class="bar"><i style="width:90%"></i></div></div>
  <div class="skill abs" style="top:130px;left:776px"><span>Some other Skill</span><div class="bar"><i style="width:73%"></i></div></div>
  <div class="skill abs" style="top:182px;left:133px"><span>CSS 3</span><div class="bar"><i style="width:98%"></i></div></div>
  <div class="skill abs" style="top:182px;left:455px"><span>NativeKit</span><div class="bar"><i style="width:80%"></i></div></div>
  <div class="skill abs" style="top:182px;left:776px"><span>Another one</span><div class="bar"><i style="width:97%"></i></div></div>
</section>

<section class="contact abs">
  <h2 class="h2 abs center" style="top:40px">KONTAKT</h2>
  <p class="abs center" style="top:76px;font-size:9.5px;line-height:16px;color:#8fa2bb">Lorem ipsum dolor sit amet, consetetur sadipscing elitr, sed diam<br>nonumy eirmod tempor invidunt ut labore et dolore magna aliquyam erat,<br>sed diam voluptua.</p>
  <svg class="abs" style="top:148px;left:528px" width="14" height="18"><path d="M7 17C2 10 1 8 1 6a6 6 0 0112 0c0 2-1 4-6 11z" fill="none" stroke="var(--orange)" stroke-width="1.4"/><circle cx="7" cy="6" r="2" fill="var(--orange)"/></svg>
  <p class="abs" style="top:165px;left:460px;width:150px;text-align:center;font-size:9.5px;line-height:16px;color:#fff">Lindenweg 12c<br>CH-9000 St.Gallen</p>
  <div class="abs" style="top:132px;left:599px;width:1px;height:95px;background:#4d6688"></div>
  <svg class="abs" style="top:148px;left:652px" width="16" height="16"><path d="M2 14l2-5 8-8 3 3-8 8z" fill="none" stroke="var(--orange)" stroke-width="1.4"/></svg>
  <p class="abs" style="top:166px;left:610px;width:104px;text-align:center;font-size:9.5px;color:#fff">timo@tira.ch</p>
  <svg class="abs" style="top:205px;left:655px" width="14" height="14"><path d="M3 1l3 3-2 2c1 2 2 3 4 4l2-2 3 3-2 2C6 13 1 8 1 3z" fill="none" stroke="var(--orange)" stroke-width="1.3"/></svg>
  <p class="abs" style="top:224px;left:605px;width:114px;text-align:center;font-size:9.5px;color:#fff">+41 70 400 12 34</p>
  <svg class="abs" style="top:224px;left:504px" width="72" height="14"><circle cx="8" cy="7" r="5" fill="#fff"/><rect x="31" y="2" width="10" height="10" fill="#fff"/><circle cx="61" cy="7" r="5" fill="#fff"/></svg>
  <p class="abs center" style="top:285px;font-size:11.5px;font-weight:700;color:#fff">SCHREIBEN SIE MIR</p>
  <div class="field abs" style="top:316px;left:375px;width:210px;padding:0 0 4px 8px">Name</div>
  <div class="field abs" style="top:316px;left:615px;width:210px;padding:0 0 4px 8px">E-Mail</div>
  <div class="field abs" style="top:346px;left:375px;width:450px;padding:0 0 8px 8px">Hier kommt Ihre Mitteilung</div>
  <div class="abs" style="top:386px;left:375px;width:450px;height:1px;background:#5c7597"></div>
  <div class="abs" style="top:444px;left:375px;width:450px;height:1px;background:#5c7597"></div>
  <a class="btn btn-blue abs" style="top:472px;left:731px;width:93px;height:35px">Absenden</a>
</section>

<footer class="footer abs">
  <div class="logo abs" style="top:22px;left:133px;font-size:18px"><i style="width:8px;height:8px"></i>TIRA</div>
  <p class="abs" style="top:28px;left:203px;font-size:9px;color:#444">© 2017 TIRA.CH &nbsp;Alle Rechte vorbehalten &nbsp;| &nbsp;Impressum &nbsp;| &nbsp;Home</p>
</footer>

</body>
</html>
```